Waterproofing/Crawlspace wrap

Car Wrap Design Brief

2000 Varlo Box Truck

-Full wrap with your own unique design
-Doors and front looking for a unique logo and decal look
-add QR Code

```html
<!DOCTYPE html>
<html lang="en">
<head>
<meta charset="utf-8">
<title>Dorian's Waterproofing – Varlo Box Truck Wrap</title>
<link rel="stylesheet" href="https://fonts.googleapis.com/css2?family=Bevan&family=Oswald:wght@500;600&display=swap">
<style>
  :root {
    --canvas: #f2f3f5;
    --box-white: #ffffff;
    --box-frame: #c9cdd2;
    --brand-blue: #2a67cf;
    --brand-blue-deep: #1d4fae;
    --brand-sky: #4f93ea;
    --brand-red: #c8262c;
    --band-red: #e2473f;
    --ink: #151515;
    --on-dark: #ffffff;
  }
  * { box-sizing: border-box; margin: 0; padding: 0; }
  html, body { width: 1200px; height: 1200px; overflow: hidden; background: var(--canvas); }
  .wrap-sheet { position: relative; width: 1200px; height: 1200px; }

  .panel {
    position: absolute;
    background: var(--box-white);
    border: 8px solid var(--box-frame);
    overflow: hidden;
  }
  .panel > * { position: absolute; }

  .estimates-band {
    background: var(--brand-blue);
    color: var(--on-dark);
    font-family: "Oswald", sans-serif;
    font-weight: 500;
    text-transform: uppercase;
    display: flex; align-items: center; justify-content: center;
    letter-spacing: 1px;
  }
  .brand-name {
    font-family: "Bevan", serif;
    color: var(--brand-red);
    text-align: center;
    letter-spacing: 3px;
    white-space: nowrap;
  }
  .brand-tag {
    font-family: "Bevan", serif;
    color: var(--ink);
    text-align: center;
    letter-spacing: 4px;
    white-space: nowrap;
  }
  .contact-band {
    background: var(--band-red);
    color: var(--on-dark);
    font-family: "Oswald", sans-serif;
    display: flex; align-items: center; gap: 14px;
    padding-left: 14px;
  }
  .contact-band .phone { font-weight: 600; letter-spacing: 1px; }
  .contact-band .divider { width: 2px; align-self: stretch; margin: 5px 0; background: var(--on-dark); }
  .contact-band .email { font-weight: 500; }

  .services-block {
    background: linear-gradient(180deg, var(--brand-blue) 0%, var(--brand-blue-deep) 100%);
  }
  .service-list {
    position: absolute;
    list-style: none;
    color: var(--on-dark);
    font-family: "Oswald", sans-serif;
    font-weight: 500;
    text-transform: uppercase;
    white-space: nowrap;
  }
  .service-list li::before { content: "• "; }

  .brand-mark {
    border-radius: 50%;
    background: radial-gradient(circle at 40% 35%, var(--brand-sky) 0%, var(--brand-blue) 55%, var(--brand-blue-deep) 100%);
    border: 8px solid var(--box-white);
  }

  /* Side A: lettering left, mark right */
  .side-a { left: 30px; top: 60px; width: 720px; height: 390px; }
  .side-b { left: 30px; top: 560px; width: 720px; height: 390px; }
  .side .estimates-band { top: 12px; height: 38px; font-size: 24px; }
  .side .brand-name { top: 60px; font-size: 56px; }
  .side .brand-tag { top: 138px; font-size: 29px; }
  .side .contact-band { top: 192px; height: 38px; }
  .side .contact-band .phone { font-size: 26px; }
  .side .contact-band .email { font-size: 15px; }
  .side .services-block { left: 12px; top: 238px; width: 680px; height: 124px; }
  .side .service-list { top: 12px; font-size: 16px; line-height: 25px; }

  .side-a .estimates-band,
  .side-a .brand-name,
  .side-a .brand-tag,
  .side-a .contact-band { left: 12px; width: 520px; }
  .side-a .brand-mark { left: 525px; top: 30px; width: 180px; height: 180px; }
  .side-a .service-list.col-1 { left: 18px; }
  .side-a .service-list.col-2 { left: 290px; }

  .side-b .estimates-band,
  .side-b .brand-name,
  .side-b .brand-tag,
  .side-b .contact-band { left: 220px; width: 472px; }
  .side-b .brand-mark { left: 14px; top: 30px; width: 200px; height: 200px; }
  .side-b .service-list.col-1 { left: 225px; }
  .side-b .service-list.col-2 { left: 460px; }

  /* Front: header board and cab door decal */
  .front-header {
    left: 790px; top: 60px; width: 380px; height: 120px;
    background: var(--brand-blue); border-color: var(--box-frame);
    display: flex; flex-direction: column; align-items: center; justify-content: center;
    color: var(--on-dark); font-family: "Oswald", sans-serif;
  }
  .front-header > * { position: static; }
  .front-header .phone { font-size: 40px; font-weight: 600; letter-spacing: 2px; line-height: 1.1; }
  .front-header .email { font-size: 16px; font-weight: 500; }

  .cab-decal {
    left: 790px; top: 210px; width: 380px; height: 140px;
    display: flex; align-items: center; justify-content: center; gap: 16px;
    border-bottom: 26px solid var(--brand-blue);
  }
  .cab-decal > * { position: static; }
  .cab-decal .dot {
    width: 46px; height: 46px; border-radius: 50%;
    background: var(--brand-blue);
  }
  .cab-decal .brand-name { font-size: 30px; letter-spacing: 2px; }

  /* Rear doors */
  .rear { left: 790px; top: 560px; width: 380px; height: 390px; }
  .rear .estimates-band { left: 10px; top: 10px; width: 344px; height: 30px; font-size: 18px; }
  .rear .brand-mark { left: 14px; top: 54px; width: 110px; height: 110px; border-width: 5px; }
  .rear .brand-name { left: 128px; width: 230px; top: 68px; font-size: 30px; letter-spacing: 2px; }
  .rear .brand-tag { left: 128px; width: 230px; top: 114px; font-size: 15px; letter-spacing: 2px; }
  .rear .contact-band { left: 10px; top: 180px; width: 344px; height: 30px; gap: 10px; padding-left: 10px; }
  .rear .contact-band .phone { font-size: 19px; }
  .rear .contact-band .email { font-size: 11px; }
  .rear .services-block { left: 10px; top: 214px; width: 344px; height: 108px; }
  .rear .service-list { top: 10px; font-size: 11px; line-height: 22px; }
  .rear .service-list.col-1 { left: 10px; }
  .rear .service-list.col-2 { left: 180px; }
  .rear .door-seam { left: 181px; top: 326px; width: 2px; height: 40px; background: var(--box-frame); }
</style>
</head>
<body>
<main class="wrap-sheet">

  <section class="panel side side-a" aria-label="Driver side box panel">
    <div class="estimates-band">Free Estimates</div>
    <div class="brand-name">DORIAN'S</div>
    <div class="brand-tag">WATERPROOFING</div>
    <div class="contact-band">
      <span class="phone">555-014-2876</span><span class="divider"></span><span class="email">dorians.services@example.com</span>
    </div>
    <div class="services-block">
      <ul class="service-list col-1">
        <li>Crawlspace Solutions</li>
        <li>Crawlspace Water Proofing</li>
        <li>Mold Remediation</li>
        <li>Dehumidifier Installation</li>
      </ul>
      <ul class="service-list col-2">
        <li>Crawlspace Encapsulation</li>
        <li>Sump Pump Installation</li>
        <li>Basement Water Froofing</li>
        <li>Basement Water Froofing</li>
      </ul>
    </div>
    <div class="brand-mark" role="img" aria-label="Brand mark"></div>
  </section>

  <section class="panel front-header" aria-label="Front header board">
    <span class="phone">555-014-2876</span>
    <span class="email">dorians.services@example.com</span>
  </section>

  <section class="panel cab-decal" aria-label="Cab door decal">
    <span class="dot"></span>
    <span class="brand-name">DORIAN'S</span>
  </section>

  <section class="panel side side-b" aria-label="Passenger side box panel">
    <div class="estimates-band">Free Estimates</div>
    <div class="brand-name">DORIAN'S</div>
    <div class="brand-tag">WATERPROOFING</div>
    <div class="contact-band">
      <span class="phone">555-014-2876</span><span class="divider"></span><span class="email">dorians.services@example.com</span>
    </div>
    <div class="services-block">
      <ul class="service-list col-1">
        <li>Crawlspace Solutions</li>
        <li>Crawlspace Water Proofing</li>
        <li>Mold Remediation</li>
        <li>Dehumidifier Installation</li>
      </ul>
      <ul class="service-list col-2">
        <li>Crawlspace Encapsulation</li>
        <li>Sump Pump Installation</li>
        <li>Basement Water Froofing</li>
        <li>Basement Water Froofing</li>
      </ul>
    </div>
    <div class="brand-mark" role="img" aria-label="Brand mark"></div>
  </section>

  <section class="panel rear" aria-label="Rear door panel">
    <div class="estimates-band">Free Estimates</div>
    <div class="brand-mark" role="img" aria-label="Brand mark"></div>
    <div class="brand-name">DORIAN'S</div>
    <div class="brand-tag">WATERPROOFING</div>
    <div class="contact-band">
      <span class="phone">555-014-2876</span><span class="divider"></span><span class="email">dorians.services@example.com</span>
    </div>
    <div class="services-block">
      <ul class="service-list col-1">
        <li>Crawlspace Solutions</li>
        <li>Crawlspace Water Proofing</li>
        <li>Mold Remediation</li>
        <li>Dehumidifier Installation</li>
      </ul>
      <ul class="service-list col-2">
        <li>Crawlspace Encapsulation</li>
        <li>Sump Pump Installation</li>
        <li>Basement Water Froofing</li>
        <li>Basement Water Froofing</li>
      </ul>
    </div>
    <div class="door-seam"></div>
  </section>

</main>
</body>
</html>
```